Plumbing Website

Design a simple 4 page website based on our provided logo and sketches. Winning designer should be willing to upgrade as needed (for additional fee). A design that includes SEO features is a plus.
I would like to see Home, , Services, Recent Jobs (set up for pictures), Contact. I like the water dropplet back ground. Please dont put logo in a box. File attached as exaple only, I am looking for a request service now button in the middle that will have a form fill to be emailed to two different addresses,
I would like to see vibrant colors. Examples of sites I like are www.maplewickplumbingandheat.com look also at www.kfv-fernvalleyplumbing.com - this site is too busy but has good seo features.

```html
<!DOCTYPE html>
<html lang="en">
<head>
<meta charset="utf-8">
<title>Ridgecrest Plumbing</title>
<link href="https://fonts.googleapis.com/css2?family=Arimo:wght@400;700&family=Cormorant+Garamond:ital,wght@0,600;1,600;1,700&family=Open+Sans:wght@400;600&family=Roboto+Condensed:wght@400&display=swap" rel="stylesheet">
<style>
:root{
  --water:#7fd0f0;
  --water-deep:#3fb0e6;
  --page:#f3f3f3;
  --blue:#0a5aa8;
  --blue-dark:#0b4b8e;
  --red:#e8282b;
  --red-dark:#c01a1e;
  --ink:#333;
  --hero:#a9c6e2;
}
*{margin:0;padding:0;box-sizing:border-box}
html,body{width:1036px;height:1200px;overflow:hidden}
body{
  background:linear-gradient(180deg,var(--water) 0%,var(--water-deep) 50%,var(--water) 100%);
  font-family:"Arimo",Arial,sans-serif;color:var(--ink);position:relative;
}
.page{position:absolute;left:44px;top:0;width:900px;height:1200px;background:var(--page)}
.abs{position:absolute}

/* header */
.header{left:0;top:0;width:900px;height:99px;background:linear-gradient(#fff,#f1f1f1)}
.brand{left:16px;top:26px;display:flex;align-items:center;gap:8px}
.brand-dot{width:18px;height:18px;border-radius:50%;background:var(--blue)}
.brand-name{font-family:"Open Sans",sans-serif;font-weight:600;font-size:19px;color:var(--blue);letter-spacing:1px;line-height:1.1}
.service-note{right:148px;top:38px;text-align:right;font-size:10.5px;color:#444;line-height:14px;white-space:nowrap}
.call{left:770px;top:21px;width:120px;height:50px}
.call svg{position:absolute;left:0;top:6px}
.call-now{position:absolute;left:40px;top:0;font-family:"Open Sans",sans-serif;font-weight:600;font-size:15px;color:#333;line-height:15px}
.toll{position:absolute;left:40px;top:14px;font-family:"Open Sans",sans-serif;font-weight:600;font-size:9.5px;letter-spacing:1.5px;color:#333}
.phone{position:absolute;left:0;top:29px;font-family:"Open Sans",sans-serif;font-weight:600;font-size:15px;color:var(--red);letter-spacing:.4px;white-space:nowrap}

/* nav */
.nav{left:-1px;top:99px;width:899px;height:37px;background:linear-gradient(#1b6fc0,var(--blue-dark));border-radius:4px 4px 0 0;display:flex}
.nav a{display:block;height:37px;line-height:37px;color:#fff;text-decoration:none;font-family:"Cormorant Garamond",serif;font-weight:600;font-size:17.5px;text-align:center;border-right:1px solid #2f7fcb;letter-spacing:.3px}
.nav a.active{background:var(--blue)}

/* hero */
.hero{left:0;top:136px;width:900px;height:301px;background:var(--hero)}
.hero-photo{position:absolute;left:420px;top:0;width:480px;height:301px;background:linear-gradient(90deg,var(--hero) 0%,#c7d3df 35%,#9aa9bd 70%,#6e86ad 100%)}
.hero-title{position:absolute;left:17px;top:30px;font-family:"Cormorant Garamond",serif;font-style:italic;font-weight:700;font-size:48px;line-height:46px;color:#111}
.hero-title .red{color:var(--red)}
.hero-title .small{font-size:42px}
.hero-copy{position:absolute;left:18px;top:131px;width:390px;font-style:italic;font-size:12.3px;line-height:18px;color:#111}
.btn-request{position:absolute;left:16px;top:236px;width:235px;height:42px;border-radius:8px;background:linear-gradient(#f24a4a,var(--red-dark));border:1px solid #b11;box-shadow:0 1px 2px rgba(0,0,0,.4);color:#fff;font-family:"Roboto Condensed",sans-serif;font-size:20px;line-height:40px;padding-left:14px}
.btn-request svg{position:absolute;right:12px;top:13px}

/* intro */
.intro-title{left:15px;top:451px;font-family:"Cormorant Garamond",serif;font-weight:600;font-size:27px;color:var(--blue);letter-spacing:.5px;white-space:nowrap}
.intro-title small{font-family:"Arimo",sans-serif;font-size:13px;color:#333;font-weight:400;letter-spacing:.3px;margin-left:8px}
.rule{left:15px;top:484px;width:862px;height:1px;background:#bbb}
.intro-copy{left:14px;top:502px;width:858px;font-size:11.6px;line-height:16.3px;color:#333;letter-spacing:.25px}
.intro-copy p+p{margin-top:16px}
.btn-more{height:23px;padding:0 8px;border-radius:3px;background:linear-gradient(#f23a3a,var(--red-dark));color:#fff;font-size:11.2px;line-height:23px;display:inline-flex;align-items:center;gap:4px;box-shadow:0 1px 1px rgba(0,0,0,.3)}

/* cards */
.card{top:663px;width:282px;height:237px;background:#fff;box-shadow:0 0 3px rgba(0,0,0,.25)}
.card h3{position:absolute;left:15px;font-family:"Cormorant Garamond",serif;font-weight:600;font-size:26px;color:#222;letter-spacing:1px}
.card h3 span{color:var(--blue)}
.card .img{position:absolute;left:12px;width:259px}
.card p{position:absolute;left:11px;top:146px;width:264px;font-family:"Open Sans",sans-serif;font-size:10.1px;line-height:14.6px;color:#333}
.card .btn-more{position:absolute;right:13px;top:205px}

/* footer */
.footer{left:0;top:935px;width:900px;height:265px;background:linear-gradient(#2e2e2e,#111)}
.footer h4{position:absolute;font-family:"Cormorant Garamond",serif;font-weight:600;font-size:25px;color:#fff;letter-spacing:.5px}
.divider{position:absolute;top:25px;width:1px;height:195px;background:#555}
.contact-info{position:absolute;left:23px;top:55px;font-size:11.6px;line-height:16.3px;color:#fff}
.contact-info .gap{margin-top:10px}
.quote{position:absolute;left:282px;width:250px;height:80px}
.quote .avatar{position:absolute;left:0;top:0;width:61px;height:71px;border:3px solid #fff;background:linear-gradient(#c9b9a8,#8d7b6a)}
.quote .who{position:absolute;left:70px;top:-1px;color:#fff;font-size:12px;font-weight:700;white-space:nowrap}
.quote .who span{font-weight:400;font-size:9.5px}
.quote .role{position:absolute;left:70px;top:14px;color:#ddd;font-size:8.8px;white-space:nowrap}
.quote .text{position:absolute;left:70px;top:30px;width:166px;color:#ddd;font-size:8.8px;line-height:13.5px;padding-left:14px}
.quote .text:before{content:"\201C";position:absolute;left:0;top:-4px;font-size:18px;font-weight:700;color:#fff}
.quote .text:after{content:"\201D";font-size:18px;font-weight:700;color:#fff;margin-left:5px;vertical-align:-8px;line-height:0}
.dots{position:absolute;left:282px;top:138px;width:232px;border-top:1px dotted #888}
.field{position:absolute;left:637px;width:210px;height:27px;background:#fff;border-radius:5px;border:1px solid #ccc;font-family:"Open Sans",sans-serif;font-size:10.5px;color:#666;padding:7px 11px;line-height:14px}
.btn-submit{position:absolute;left:772px;top:211px;width:78px;height:23px;border-radius:3px;background:linear-gradient(#f23a3a,var(--red-dark));color:#fff;font-family:"Open Sans",sans-serif;font-weight:600;font-size:12.5px;text-align:center;line-height:23px}
</style>
</head>
<body>
<div class="page">

  <header class="abs header">
    <div class="abs brand">
      <span class="brand-dot"></span>
      <span class="brand-name">RIDGECREST<br>PLUMBING</span>
    </div>
    <div class="abs service-note">24/7 EMERGENCY SERVICE<br>FREE EVALUATION &amp; CONSULTATION</div>
    <div class="abs call">
      <svg width="32" height="12" viewBox="0 0 32 12"><path d="M2 10 C2 3 30 3 30 10 L24 10 L23 7 C18 5 14 5 9 7 L8 10 Z" fill="#444"/></svg>
      <div class="call-now">Call Now</div>
      <div class="toll">TOLL FREE</div>
      <div class="phone">800·555·0142</div>
    </div>
  </header>

  <nav class="abs nav">
    <a class="active" style="width:121px">HOME</a>
    <a style="width:147px">ABOUT US</a>
    <a style="width:141px">SERVICES</a>
    <a style="width:174px">RECENT JOBS</a>
    <a style="width:174px;border-right:0">CONTACT US</a>
  </nav>

  <section class="abs hero">
    <div class="hero-photo" role="img" aria-label="Photo of a smiling plumber fitting pipes under a sink"></div>
    <h1 class="hero-title"><span class="red">Plumbers,</span> do you<br><span class="small">need more work?</span></h1>
    <p class="hero-copy">Lorem Ipsum has been the industry's standard dummy text ever since the 1500s, when an unknown printer took a galley of type and scrambled it to make a type specimen book. It has survived not only five centuries, but also the leap into electronic typesetting, remaining essentially unchanged</p>
    <div class="btn-request">Request Service Now
      <svg width="18" height="16" viewBox="0 0 18 16"><path d="M1 1l7 7-7 7M9 1l7 7-7 7" fill="none" stroke="#fff" stroke-width="2.4"/></svg>
    </div>
  </section>

  <h2 class="abs intro-title">Our Family Serving Your Family <small>Family Owned and Operated Since 1995</small></h2>
  <div class="abs rule"></div>
  <div class="abs intro-copy">
    <p>Ridgecrest Plumbing is the industry leader in the area.&nbsp; We are a Plumbing, Drain Cleaning, and General Engineering contractors, providing excellent customer service and helping homeowners to live more comfortable and healthy lives. If you are looking for a Plumber in Cedar Valley then call on Ridgecrest Plumbing as your Plumbing Contractor. When the water heater bursts or the bathroom is flooding, do you want the best plumber available, or do you want the cheapest?&nbsp;&nbsp; At Ridgecrest Plumbing,</p>
    <p>we know that the best plumber does world-class work, is fully licensed and insured, is available 24/7 – including during emergencies – and somehow combines world-class equipment and service with world-class affordability.</p>
  </div>
  <div class="abs btn-more" style="left:796px;top:627px">read more
    <svg width="9" height="8" viewBox="0 0 9 8"><path d="M1 1l3 3-3 3M5 1l3 3-3 3" fill="none" stroke="#fff" stroke-width="1.4"/></svg></div>

  <article class="abs card" style="left:12px">
    <h3 style="top:0"><span>Plumb</span>ing</h3>
    <div class="img" role="img" aria-label="Photo of a plumber working under a kitchen sink" style="top:36px;height:105px;background:linear-gradient(135deg,#e8ecef,#c3cbd3 60%,#8b9bb0)"></div>
    <p>Contrary to popular belief, Lorem Ipsum is not simply random text. It has roots in a piece of classical Latin literature from 45 BC, making it over 2000 years old. Daniel Foster,</p>
    <div class="btn-more">read more <svg width="9" height="8" viewBox="0 0 9 8"><path d="M1 1l3 3-3 3M5 1l3 3-3 3" fill="none" stroke="#fff" stroke-width="1.4"/></svg></div>
  </article>

  <article class="abs card" style="left:309px">
    <h3 style="top:6px"><span>Drain</span> Cleaning</h3>
    <div class="img" role="img" aria-label="Photo of a plumber clearing a bathroom sink drain" style="top:42px;height:98px;background:linear-gradient(135deg,#dfe4ea,#b7c2cf 55%,#3a5f9a)"></div>
    <p>Contrary to popular belief, Lorem Ipsum is not simply random text. It has roots in a piece of classical Latin literature from 45 BC, making it over 2000 years old. Daniel Foster,</p>
    <div class="btn-more">read more <svg width="9" height="8" viewBox="0 0 9 8"><path d="M1 1l3 3-3 3M5 1l3 3-3 3" fill="none" stroke="#fff" stroke-width="1.4"/></svg></div>
  </article>

  <article class="abs card" style="left:606px">
    <h3 style="top:4px"><span>General</span> Engineering</h3>
    <div class="img" role="img" aria-label="Photo of a road crew working on a street with traffic cones" style="top:42px;height:98px;background:linear-gradient(160deg,#a8b4c0,#8a8f92 55%,#6c6a66)"></div>
    <p>Contrary to popular belief, Lorem Ipsum is not simply random text. It has roots in a piece of classical Latin literature from 45 BC, making it over 2000 years old. Daniel Foster,</p>
    <div class="btn-more">read more <svg width="9" height="8" viewBox="0 0 9 8"><path d="M1 1l3 3-3 3M5 1l3 3-3 3" fill="none" stroke="#fff" stroke-width="1.4"/></svg></div>
  </article>

  <footer class="abs footer">
    <h4 style="left:23px;top:15px">Contact Us</h4>
    <div class="contact-info">
      <b>Our Office:</b><br>4210 Alder Ridge Rd Suite 210<br>Pine Crest, CA 91999
      <div class="gap"><b>Contact Info:</b><br>951-555-0178<br>service@ridgecrestplumbing.com</div>
      <div class="gap"><b>24 Hours a Day<br>7 Days a Week</b></div>
    </div>
    <div class="divider" style="left:236px"></div>

    <h4 style="left:281px;top:12px">Customer Says</h4>
    <div class="quote" style="top:55px">
      <div class="avatar" role="img" aria-label="Customer portrait"></div>
      <div class="who">Halvora, <span>Diagnostics</span></div>
      <div class="role">Medical Education and Lead Generator</div>
      <div class="text">Lorem ipsum is simply dummy text of the printing type setting industries of dummy text printing text</div>
    </div>
    <div class="dots"></div>
    <div class="quote" style="top:155px">
      <div class="avatar" role="img" aria-label="Customer portrait"></div>
      <div class="who">Halvora, <span>Diagnostics</span></div>
      <div class="role">Medical Education and Lead Generator</div>
      <div class="text">Lorem ipsum is simply dummy text of the printing type setting industries of dummy text printing text</div>
    </div>
    <div class="divider" style="left:571px"></div>

    <h4 style="left:637px;top:14px">Quick Enquiry</h4>
    <div class="field" style="top:58px">Your Name</div>
    <div class="field" style="top:92px">Email</div>
    <div class="field" style="top:129px;height:62px;line-height:16px">Tell Us About Your Project and your Requirment</div>
    <div class="btn-submit">Submit</div>
  </footer>

</div>
</body>
</html>
```